creative pack design with extended budget for Nobrelia coffee product

- we need a packing design for a new product of coffee for our company Mbelo Tiru located in Uganda.
- specialty Arabica coffee grown at slopes of Mountain Elgon with rich volcanic soils located in Eastern region of Uganda.
-  we have a logo already made and has registered in Uganda. our logo colors are mixture between a lot of brown color and yellow. vacuum  plastic bags.
- there is no restrictions towards your imagination .
-  all details available
- we will launch our product through phases ;
- phase 1 is  a ground coffee : ( Turkish coffee )  2 degrees of roasting which are ( medium dark , light ) of 250 grm
b) roasted beans: 2 degrees ( medium, dark) of 250 grm & 1000 grm
- we need also to highlight the eastern spirit of Turkish coffee
- we  need designs, the info and color only will be changed depending on previous classifications

Target Market(s)
Arab countries, Turkey , Uganda, Europe
Colors
Designer to choose colors to be used in the design.
Requirements
Nice to have
- about nature , Elgon mountain , farmers, freshness, distinctive product, soul of east such as decorated cup of Turkish coffee . these just an ideas but there is no restrictions on your imagination

```html
<!DOCTYPE html>
<html lang="en">
<head>
<meta charset="utf-8">
<title>Nobrelia Turkish Ground Coffee – Pack Fronts</title>
<link href="https://fonts.googleapis.com/css2?family=Marcellus&family=Crimson+Pro:wght@400;500&display=swap" rel="stylesheet">
<style>
  :root {
    --canvas-bg: #eceae4;
    --pack-white: #ffffff;
    --paper-light: #fbeed2;
    --paper-mid: #f3d9a8;
    --paper-edge: #e79a62;
    --ink: #1c140d;
    --dark-roast: #35230f;
    --light-roast: #d38957;
    --light-roast-line: #c97c46;
    --label-text: #fbf2e4;
  }
  * { box-sizing: border-box; margin: 0; padding: 0; }
  html, body { width: 1200px; height: 783px; overflow: hidden; }
  body {
    background: var(--canvas-bg);
    position: relative;
    font-family: "Crimson Pro", Georgia, serif;
  }
  .pack {
    position: absolute;
    top: 172px;
    width: 318px;
    height: 498px;
    background: var(--pack-white);
    border-radius: 4px;
    box-shadow: 0 12px 24px rgba(0,0,0,0.08);
  }
  .pack--medium-dark { left: 218px; --roast: var(--dark-roast); --art: #3a2a1a; }
  .pack--light { left: 650px; --roast: var(--light-roast); --art: var(--light-roast-line); }

  .pack__print {
    position: absolute;
    left: 28px;
    top: 0;
    width: 266px;
    height: 460px;
    border-radius: 0 0 12px 12px;
    overflow: hidden;
    background:
      radial-gradient(ellipse 70% 60% at 50% 48%, var(--paper-light) 0%, var(--paper-mid) 60%, var(--paper-edge) 100%);
  }
  .pack__top-band {
    position: absolute; left: 0; top: 0; width: 100%; height: 20px;
    background: var(--roast);
  }
  .brand {
    position: absolute; left: 0; top: 36px; width: 100%;
    text-align: center;
  }
  .brand__dot {
    display: block; width: 48px; height: 48px; margin: 0 auto 6px;
    border-radius: 50%; background: #7a4a2e;
  }
  .brand__name {
    font-family: "Marcellus", Georgia, serif;
    font-size: 24px; color: #5b3520; letter-spacing: 1px;
  }
  .pack__artwork {
    position: absolute; left: 58px; top: 148px; width: 152px; height: 144px;
    border-radius: 4px;
    background: linear-gradient(180deg, rgba(0,0,0,0) 0%, var(--art) 260%);
    opacity: 0.55;
  }
  .roast-tag {
    position: absolute; left: 74px; top: 298px; width: 124px; height: 42px;
    border-radius: 10px; background: var(--roast);
    color: var(--label-text);
    display: flex; align-items: center; justify-content: center;
    font-size: 18px;
  }
  .pack--light .roast-tag { font-size: 27px; }
  .roast-tag__tail {
    position: absolute; left: 56px; top: 40px;
  }
  .product-name {
    position: absolute; left: 0; top: 362px; width: 100%;
    text-align: center;
    font-family: "Marcellus", Georgia, serif;
    color: var(--ink);
    font-size: 21px; line-height: 19px; letter-spacing: 0.5px;
  }
  .net-weight {
    position: absolute; left: 0; bottom: 0; width: 100%; height: 40px;
    background: var(--roast); color: var(--label-text);
    display: flex; align-items: center; justify-content: center;
    font-size: 15px; letter-spacing: 0.3px;
  }
</style>
</head>
<body>

  <section class="pack pack--medium-dark">
    <div class="pack__print">
      <div class="pack__top-band"></div>
      <div class="brand">
        <span class="brand__dot"></span>
        <span class="brand__name">Nobrelia</span>
      </div>
      <div class="pack__artwork" role="img" aria-label="Line illustration of an Eastern mosque skyline with domes, minarets and crescent moon"></div>
      <div class="roast-tag">medium dark
        <svg class="roast-tag__tail" width="14" height="14" viewBox="0 0 14 14"><path d="M0 0 H14 L3 14 Z" fill="var(--roast)"/></svg>
      </div>
      <h2 class="product-name">TURKISH<br>GROUND COFFEE</h2>
      <div class="net-weight">Net 250 grm</div>
    </div>
  </section>

  <section class="pack pack--light">
    <div class="pack__print">
      <div class="pack__top-band"></div>
      <div class="brand">
        <span class="brand__dot"></span>
        <span class="brand__name">Nobrelia</span>
      </div>
      <div class="pack__artwork" role="img" aria-label="Line illustration of an Eastern mosque skyline with domes, minarets and crescent moon"></div>
      <div class="roast-tag">light
        <svg class="roast-tag__tail" width="14" height="14" viewBox="0 0 14 14"><path d="M0 0 H14 L3 14 Z" fill="var(--roast)"/></svg>
      </div>
      <h2 class="product-name">TURKISH<br>GROUND COFFEE</h2>
      <div class="net-weight">Net 250 grm</div>
    </div>
  </section>

</body>
</html>
```